4D Hush Little Nest Luxury Ultrasound Billboard

Design a HIGH-END, MODERN billboard for my private prenatal ultrasound studio, 4D Hush Little Nest, located in Pace, Florida.
This billboard will be viewed by drivers traveling at highway speeds, so it must be extremely clean, simple, and readable within 6 seconds.
About My Business
4D Hush Little Nest is a private prenatal ultrasound studio specializing in:
Highest technology 4D/HD Ultrasounds
Early Gender Determination
Pregnancy Confirmation
I have been serving families for nearly 10 years and is known for creating a memorable experience, not just an ultrasound appointment.
Design Style
I DO NOT want:
Flowers
Leaves
Swirls
Glitter
Hearts everywhere
Busy backgrounds
Generic maternity stock graphics
I DO want:
Modern
Luxury
Upscale
Clean
Professional
Eye-catching
Premium medical spa feel
Colors
Use colors from my logo:
LOGO Green ( or a deep green)
Black
White
Soft Gold accents
Images:
Incorporate my professional headshot in a clean, modern way, logo, and the ultrasound images
Text
Keep wording minimal.
Primary Headline ( OPEN TO IDEAS) :
EXAMPLES ( WOULD RATHER SOMETHING MORE CATCHY)
" ADVANCED IMAGING. UNFORGETTABLE MOMENTS"
"MEET YOUR BABY BEFORE BIRTH"
Under headline:
4D Ultrasound • Early Gender • Pregnancy Confirmation
Business Name:
4D Hush Little Nest
Private Prenatal Ultrasound Studio
Phone Number:
850-471-3905
Important
This billboard must be readable in 5–6 seconds from a moving vehicle.
Less text is better.
The phone number and business name must be visible from a distance.
The design should feel like a premium brand that immediately tells expecting parents:
“This is where I go to see my baby.”
Files Provided
Official logo
Headshot
Ultrasound images
Don’t make this look like a medical office billboard.
Make it look like a luxury baby experience billboard. That’s what separates 4D Hush Little Nest from hospitals, OB offices, and all the new studios popping up around you. The emotional connection is what gets moms to book. ❤️
Billboard Size - 10.6” x 36”

```html
<!DOCTYPE html>
<html lang="en">
<head>
<meta charset="utf-8">
<title>4D Hush Little Nest – Billboard</title>
<link rel="stylesheet" href="https://fonts.googleapis.com/css2?family=Playfair+Display:wght@600;800&family=Great+Vibes&family=Poppins:wght@400;500;700&display=swap">
<style>
  :root {
    --stage: #7b7b7b;
    --ink: #0d0d0d;
    --panel: #131313;
    --white: #ffffff;
    --gold: #c9a24a;
    --gold-light: #e3c57a;
    --gold-deep: #9c7a2c;
    --green: #2f4a2c;
  }
  * { margin: 0; padding: 0; box-sizing: border-box; }
  html, body { width: 979px; height: 1200px; overflow: hidden; }
  body { background: var(--stage); position: relative; font-family: "Poppins", sans-serif; }

  .billboard {
    position: absolute; left: 39px; top: 469px;
    width: 900px; height: 262px;
    background: linear-gradient(100deg, #1a1a1a 0%, var(--panel) 45%, #0b0b0b 100%);
    overflow: hidden;
    box-shadow: 0 6px 16px rgba(0,0,0,.35);
  }

  .ultrasound-art { position: absolute; inset: 0; }

  .brand-box {
    position: absolute; left: 43px; top: 26px; width: 120px; height: 59px;
    border: 1.5px solid #5d5d5d; border-radius: 6px;
    display: flex; align-items: center; justify-content: center; text-align: center;
  }
  .brand-name {
    font-family: "Poppins", sans-serif; font-weight: 700; font-size: 13px; line-height: 1.15;
    color: var(--gold);
  }

  .services { position: absolute; left: 44px; top: 98px; list-style: none; }
  .services li { display: flex; align-items: flex-start; color: var(--white); font-size: 15px; line-height: 17px; margin-bottom: 8px; }
  .services svg { width: 18px; height: 18px; margin-right: 18px; flex: none; }

  .headline { position: absolute; left: 170px; top: 0; width: 400px; height: 200px; font-weight: normal; }
  .headline .lead {
    position: absolute; left: 0; right: 0; top: 22px;
    display: flex; align-items: center; justify-content: center; gap: 6px;
    font-family: "Playfair Display", serif; font-weight: 600; font-size: 36px; line-height: 40px;
    color: var(--white); letter-spacing: -.5px;
  }
  .headline .rule { display: block; width: 78px; height: 1px; background: var(--gold-deep); flex: none; }
  .headline .main {
    position: absolute; left: 0; right: 0; top: 47px; text-align: center;
    font-family: "Playfair Display", serif; font-weight: 800; font-size: 97px;
    line-height: 97px; letter-spacing: -2px;
    background: linear-gradient(180deg, var(--gold-light) 0%, var(--gold) 50%, var(--gold-deep) 100%);
    -webkit-background-clip: text; background-clip: text; color: transparent;
  }
  .headline .script {
    position: absolute; left: 0; right: 0; top: 122px; text-align: center;
    font-family: "Great Vibes", cursive; font-size: 58px; line-height: 60px; color: var(--white);
  }

  .contact-band {
    position: absolute; left: 0; bottom: 0; width: 560px; height: 66px;
    background: linear-gradient(90deg, #d4b066 0%, var(--gold-light) 40%, var(--gold) 100%);
    display: flex; align-items: center; padding-left: 42px;
  }
  .phone-icon { width: 32px; height: 32px; margin-right: 4px; }
  .phone { font-weight: 700; font-size: 39px; color: var(--ink); letter-spacing: -.5px; }
  .divider { width: 1px; height: 34px; background: var(--ink); margin: 0 12px; opacity: .7; }
  .tagline { font-size: 15px; font-weight: 500; line-height: 16px; color: var(--ink); }
</style>
</head>
<body>
  <section class="billboard" aria-label="4D Hush Little Nest billboard">
    <svg class="ultrasound-art" viewBox="0 0 900 262" width="900" height="262">
      <defs>
        <radialGradient id="scanTone" cx="70%" cy="40%" r="70%">
          <stop offset="0" stop-color="#c98a78"/>
          <stop offset=".55" stop-color="#9a4f42"/>
          <stop offset="1" stop-color="#4a1a14"/>
        </radialGradient>
        <linearGradient id="portraitTone" x1="0" y1="0" x2="0" y2="1">
          <stop offset="0" stop-color="#d8c28e"/>
          <stop offset=".45" stop-color="#caa890"/>
          <stop offset="1" stop-color="#2f4a2c"/>
        </linearGradient>
      </defs>
      <g role="img" aria-label="4D ultrasound image of a baby's face">
        <path d="M640 0 Q600 95 606 262 L900 262 L900 0 Z" fill="url(#scanTone)"/>
      </g>
      <path d="M640 0 Q600 95 606 262" fill="none" stroke="#c9a24a" stroke-width="2"/>
      <g role="img" aria-label="Headshot of the studio owner in green scrubs">
        <rect x="536" y="75" width="112" height="187" rx="30" fill="url(#portraitTone)" opacity=".9"/>
      </g>
    </svg>

    <div class="brand-box">
      <span class="brand-name">4D Hush<br>Little Nest</span>
    </div>

    <ul class="services">
      <li>
        <svg viewBox="0 0 18 18"><rect x="2" y="2" width="14" height="10" rx="1.5" fill="none" stroke="#c9a24a" stroke-width="1.6"/><path d="M6 16h6M9 12v4" stroke="#c9a24a" stroke-width="1.6"/></svg>
        4D Ultrasound
      </li>
      <li>
        <svg viewBox="0 0 18 18"><circle cx="5.5" cy="10" r="3.5" fill="none" stroke="#c9a24a" stroke-width="1.6"/><circle cx="12.5" cy="7" r="3.5" fill="none" stroke="#c9a24a" stroke-width="1.6"/><path d="M8 7.5l3-3.5M9 4h2.2v2.2M12.5 10.5v6M10.5 14h4" stroke="#c9a24a" stroke-width="1.4" fill="none"/></svg>
        Early Gender
      </li>
      <li>
        <svg viewBox="0 0 18 18"><path d="M3 15l10-10 2 2-10 10z" fill="#c9a24a"/><rect x="8" y="8" width="3" height="2" fill="#131313" transform="rotate(-45 9.5 9)"/></svg>
        Pregnancy<br>Confirmation
      </li>
    </ul>

    <h1 class="headline">
      <span class="lead"><span class="rule"></span>MEET YOUR<span class="rule"></span></span>
      <span class="main">BABY</span>
      <span class="script">Before Birth</span>
    </h1>

    <div class="contact-band">
      <svg class="phone-icon" viewBox="0 0 32 32">
        <circle cx="16" cy="16" r="14" fill="#0d0d0d"/>
        <path d="M11 9c1-1 2-.5 2.6.5l1.2 2.2c.4.8.2 1.6-.5 2.1l-.9.7c.8 1.8 2.2 3.2 4 4l.7-.9c.5-.7 1.3-.9 2.1-.5l2.2 1.2c1 .6 1.5 1.6.5 2.6l-1 1c-1.4 1.4-4.6.6-7.6-2.4S9.6 11.4 11 10z" fill="#e3c57a"/>
      </svg>
      <span class="phone">850-471-3905</span>
      <span class="divider"></span>
      <span class="tagline">Private Prenatal<br>Ultrasound Studio</span>
    </div>
  </section>
</body>
</html>
```